Harborlight Skipper Services LLC

I'd like business cards with a logo and words to describe my services and qualifications. I want to emphasize the wide variety of services offered and my professional qualifications. Words to include "Harborlight Skipper Services LLC", "Motor and Sailing Vessel Delivery, Charter, Surveys, Towing and Instruction". Qualifications I would like to include are "Captain Dale Movik, NMRB Master Mariner, 200 ton, Ocean". Include address, phone and email: "48213 Pellowmere Lane, Wrenhaven Landing, MD 22417, (C) 410-555-0187, HarborlightSkipperServices@quillmail.example"

Target Market(s)

I am targeting recreational boaters and commercial customers that need people to operate their boats for charter or delivery to another location.

Industry/Entity Type

boat selling/buying, boat charter, boat recreation

Logo Text

"Motor and Sailing Vessel Delivery, Charters, Surveys, Towing and Instruction"

Requirements
Must have
• A professional and nautical look.
Nice to have
• May be nice to have a muted chart as the background design
Should not have
• colors or design that obscure the message of offering a wide range of professional boat captain services

```html
<!DOCTYPE html>
<html lang="en">
<head>
<meta charset="utf-8">
<title>Harborlight Skipper Services LLC – Business Cards</title>
<link rel="stylesheet" href="https://fonts.googleapis.com/css2?family=Libre+Baskerville:wght@700&family=Montserrat:wght@400;500;700&family=Open+Sans:wght@400&display=swap">
<style>
  :root {
    --stage: #2d2a36;
    --navy: #1b2565;
    --navy-deep: #161f56;
    --navy-soft: #27327a;
    --gold: #d3a83f;
    --gold-light: #f1d27a;
    --paper: #eeeeec;
    --paper-shade: #e2e2e0;
    --white: #ffffff;
  }
  * { margin: 0; padding: 0; box-sizing: border-box; }
  html, body { width: 943px; height: 1200px; overflow: hidden; background: var(--stage); }
  .sheet { position: relative; width: 943px; height: 1200px; }

  .card {
    position: absolute; left: 126px; width: 692px; height: 390px; overflow: hidden;
    box-shadow: 18px 22px 34px rgba(0,0,0,0.45);
  }
  .card--front { top: 169px; background: var(--paper); }
  .card--back { top: 641px; background: var(--navy); }

  .chart-backdrop { position: absolute; inset: 0; }
  .chart-backdrop--paper { background: radial-gradient(ellipse at 60% 45%, var(--paper) 0%, var(--paper-shade) 100%); }
  .chart-backdrop--navy { background: radial-gradient(ellipse at 50% 50%, var(--navy-soft) 0%, var(--navy-deep) 100%); }

  .header-band {
    position: absolute; left: 0; top: 0; width: 100%; height: 127px;
    background: linear-gradient(180deg, var(--navy-soft) 0%, var(--navy) 100%);
  }
  .gold-rule {
    position: absolute; left: 0; top: 127px; width: 100%; height: 5px;
    background: linear-gradient(90deg, var(--gold), var(--gold-light), var(--gold));
  }

  .brand-mark { position: absolute; border: 2px solid var(--gold); border-radius: 50%; }
  .header-band .brand-mark { left: 27px; top: 16px; width: 92px; height: 92px; }
  .brand-name {
    position: absolute; color: var(--white);
    font-family: "Montserrat", sans-serif; font-weight: 500; letter-spacing: 0.05em;
  }
  .header-band .brand-name { left: 146px; top: 34px; font-size: 21px; line-height: 28px; }

  .header-divider { position: absolute; left: 422px; top: 10px; width: 1px; height: 107px; background: var(--white); }
  .services {
    position: absolute; left: 439px; top: 25px; color: var(--white);
    font-family: "Montserrat", sans-serif; font-weight: 400; font-size: 14.5px; line-height: 25px;
    text-transform: uppercase;
  }

  .captain-name {
    position: absolute; left: 47px; top: 163px; color: var(--navy);
    font-family: "Libre Baskerville", serif; font-weight: 700; font-size: 31px; white-space: nowrap;
  }
  .name-rule { position: absolute; left: 51px; top: 209px; width: 277px; height: 1.5px; background: var(--navy); }
  .credentials {
    position: absolute; left: 47px; top: 215px; color: var(--navy);
    font-family: "Open Sans", sans-serif; font-size: 23px; line-height: 33px;
  }

  .contact-list { position: absolute; right: 74px; top: 236px; list-style: none; text-align: right; }
  .contact-list li {
    color: var(--navy); font-family: "Montserrat", sans-serif; font-size: 16px; line-height: 28px; white-space: nowrap;
  }
  .contact-list .phone { font-weight: 700; margin-top: 4px; }
  .contact-list .email { margin-top: 6px; }
  .contact-icon { position: absolute; left: 638px; fill: var(--navy); }

  .card--back .brand-mark { left: 238px; top: 53px; width: 216px; height: 216px; border-width: 3px; }
  .card--back .brand-name { left: 0; width: 100%; top: 298px; text-align: center; font-size: 23px; }
</style>
</head>
<body>
<main class="sheet">
  <section class="card card--front">
    <div class="chart-backdrop chart-backdrop--paper" role="img" aria-label="Muted antique nautical chart printed faintly on white paper"></div>
    <header class="header-band">
      <div class="chart-backdrop chart-backdrop--navy" role="img" aria-label="Faint antique nautical chart on navy"></div>
      <div class="brand-mark"></div>
      <div class="brand-name">Harborlight<br>Skipper Services LLC</div>
      <div class="header-divider"></div>
      <p class="services">Motor and sailing vessel<br>delivery, charter, surveys,<br>towing and instruction</p>
    </header>
    <div class="gold-rule"></div>

    <h1 class="captain-name">Captain Dale Movik</h1>
    <div class="name-rule"></div>
    <p class="credentials">NMRB Master Mariner<br>200 ton, Ocean</p>

    <ul class="contact-list">
      <li>48213 Pellowmere Lane</li>
      <li>Wrenhaven Landing, MD 22417</li>
      <li class="phone">410-555-0187</li>
      <li class="email">HarborlightSkipperServices@quillmail.example</li>
    </ul>

    <svg class="contact-icon" style="top:248px" width="26" height="32" viewBox="0 0 26 32" aria-hidden="true">
      <path d="M13 0C6 0 1 5 1 12c0 8 12 20 12 20s12-12 12-20C25 5 20 0 13 0zm0 17a5 5 0 1 1 0-10 5 5 0 0 1 0 10z"/>
    </svg>
    <svg class="contact-icon" style="top:297px" width="28" height="28" viewBox="0 0 28 28" aria-hidden="true">
      <path d="M16 2h4c2 0 3 1 3 3v18c0 2-1 3-3 3h-4v-4h3V6h-3z"/>
      <path d="M12 9a6 6 0 0 0 0 10" stroke="#1b2565" stroke-width="2" fill="none"/>
      <path d="M8 6a10 10 0 0 0 0 16" stroke="#1b2565" stroke-width="2" fill="none"/>
    </svg>
    <svg class="contact-icon" style="top:335px" width="30" height="22" viewBox="0 0 30 22" aria-hidden="true">
      <rect x="0" y="0" width="30" height="22" rx="3"/>
      <path d="M3 4l12 9 12-9" stroke="#eeeeec" stroke-width="2.5" fill="none"/>
    </svg>
  </section>

  <section class="card card--back">
    <div class="chart-backdrop chart-backdrop--navy" role="img" aria-label="Faint antique nautical chart on navy"></div>
    <div class="brand-mark"></div>
    <div class="brand-name">Harborlight Skipper Services LLC</div>
  </section>
</main>
</body>
</html>
```